Business Card Makeover. Recreate a sleek modern design for our business card.

DO NOT COPY OUR CURRENT DESIGN. MUST BE ONE SIDED BUSINESS CARD.
Create a new business card design, using our new logo. Attached is a sample of our current design and new logo. Please note the address and email will change. The new address is 417 Corvell West Palm Beach 33472 and our website will be www.talvendrake.example.

We are an architectural and interior design firm. We prefer a clean modern look. Something that is refined and emulates excellence.

Industry/Entity Type

Architecture

Contact Information for Business Card

clean modern look, please do not copy our attached design.

Font styles to use
Other font styles liked:
• see attached business card font

Colors

Designer to choose colors to be used in the design.

Requirements
Must have
• Must have a modern appeal and resemble our current branding.
Nice to have
• modern font, our logo, legible name and titles progressive design
Should not have
• Do not add colors not reflected in our branding. Should not look like our current card.

```html
<!DOCTYPE html>
<html lang="en">
<head>
<meta charset="utf-8">
<title>Talven Drake + Partners – Business Card</title>
<link rel="stylesheet" href="https://fonts.googleapis.com/css2?family=Open+Sans:wght@400;500;600&display=swap">
<style>
  :root {
    --backdrop: #474747;
    --card: #ffffff;
    --ink: #222222;
    --muted: #8c8c8c;
    --brand-blue: #0f72bd;
    --brand-grey: #a3a3a3;
  }
  * { margin: 0; padding: 0; box-sizing: border-box; }
  html, body {
    width: 1200px; height: 900px; overflow: hidden;
    background: var(--backdrop);
    font-family: "Open Sans", Arial, sans-serif;
  }
  .business-card {
    position: absolute; left: 286px; top: 267px;
    width: 629px; height: 367px;
    background: var(--card);
    border-radius: 29px;
    overflow: hidden;
  }
  .brand { position: absolute; left: 341px; top: 26px; display: flex; align-items: center; gap: 10px; }
  .brand-dot { width: 52px; height: 52px; border-radius: 50%; background: var(--brand-blue); }
  .brand-name {
    font-weight: 500; color: var(--ink); line-height: 1;
    font-size: 22px; letter-spacing: 0.5px;
  }
  .brand-name small { display: block; font-size: 8px; letter-spacing: 2.5px; text-align: right; margin-top: 3px; }
  .person { position: absolute; left: 30px; top: 171px; }
  .person-name { font-size: 21px; font-weight: 400; color: var(--ink); line-height: 1.1; }
  .person-name .credentials { font-size: 15px; }
  .person-title { font-size: 15px; color: var(--brand-blue); letter-spacing: 0.6px; margin-top: 2px; }
  .title-rule { position: absolute; left: 260px; right: 0; top: 207px; height: 2px; background: var(--brand-blue); }
  .contact-list { position: absolute; left: 31px; top: 252px; list-style: none; }
  .contact-list li {
    display: flex; align-items: center; gap: 10px;
    font-size: 13px; color: var(--muted); height: 22px;
  }
  .contact-list svg { width: 12px; height: 12px; fill: var(--brand-blue); }
  .address { position: absolute; right: 34px; top: 295px; font-size: 15px; color: var(--muted); }
  .footer-band { position: absolute; left: 0; bottom: 0; width: 629px; height: 33px; }
  .license {
    position: absolute; left: 464px; bottom: 6px;
    font-size: 15px; color: #ffffff; letter-spacing: 0.3px;
  }
</style>
</head>
<body>
  <article class="business-card">
    <div class="brand">
      <span class="brand-dot"></span>
      <div class="brand-name">TALVEN DRAKE<small>+ PARTNERS</small></div>
    </div>

    <div class="person">
      <h1 class="person-name">Marisa Quell, <span class="credentials">AIA, LEED</span></h1>
      <p class="person-title">Partner&nbsp;I&nbsp; Project Architect</p>
    </div>
    <div class="title-rule"></div>

    <ul class="contact-list">
      <li>
        <svg viewBox="0 0 12 12"><path d="M1 4c0-2 10-2 10 0v1H8.5V4h-5v1H1zM3 6h6l1.5 4h-9z"/></svg>
        561.555.0142
      </li>
      <li>
        <svg viewBox="0 0 12 12"><path d="M3 1h5v3H3zM1 5h10v6H1z"/></svg>
        561.555.0187
      </li>
      <li>
        <svg viewBox="0 0 12 12"><path d="M1 2.5h10v7H1z"/><path d="M1.5 3l4.5 3.5L10.5 3" fill="none" stroke="#fff" stroke-width="1"/></svg>
        marisa@talvendrake.example
      </li>
    </ul>

    <p class="address">417 Corvell West Palm Beach 33472</p>

    <svg class="footer-band" viewBox="0 0 629 33" preserveAspectRatio="none">
      <polygon points="0,0 446,0 437,33 0,33" fill="var(--brand-blue)"/>
      <polygon points="451,0 629,0 629,33 442,33" fill="var(--brand-grey)"/>
    </svg>
    <p class="license">LIC.# AA41870253</p>
  </article>
</body>
</html>
```